SaaS / Consulting / Solution website redesign

We need a website design that:
- Is completely different than our current design : https://velmorahub.com
- Has a very minimal amount of copy
- Changes our positioning from a SaaS application to a solutions company. Solutions company means that we help our customers solve their problems with consulting, training, and tools. An example of a solutions company is here: https://pastcache.net/web/20130111103320/http://www.quintorabuild.com:80/
- Does not make us look like a start up
- Is more people oriented than technology oriented

We need a designer that:
- Is a rebel at heart
- Is a minimalist
- Tells us why our current site sucks
- Can disagree with us
- Can also do copywriting or already has a copywriter that can help
- Is ok with saying we have capability that we don't in order to see if people actually want that
- Can understand the difference between our grand vision and where we need to focus ourselves today in order to get there

Who we are:
- Entrepreneurs
- Programmers
- Consultants
- Investors

Here's our design goals:
#1 Get customers, investors, employers, and partners excited about our unique and clearly articulated value proposition
#2 Get people to contact us asking for help with their programs
#3 Position ourselves as an expert in the skills based volunteering, mentorship, and group collaboration
#4 Make it easy for people, who already know who we are, to register online

What our grand vision is:
- Create a marketplace where any person can go to our site and find time with anyone they need to meet with. Whether that is their hair stylist, school advisor, parent of your kids class, dentist, attorney, etc.

What will you get if you win:
- In addition to the prize of this project we will have many landing pages and other revisions we will need in the future. We currently don't have a designer or copywriter and need to add that capability to our team

Who do we need to appeal to:
- Directors that are launching innovative programs inside organizations
- IT personnel who are trying to disqualify our technology so they don't have to support it or deal with it when it doesn't go well
- Enterprise IT architects who don't want our product being on its own island within their organization totally incompatible with everything else. Architects which are trying to assess how our platform will co-exist with all their other platforms
- Vice Presidents who want to help their directors understand that we don't have enough experience to help them
- Program managers who have to juggle a million things and need a tool that actually helps instead of confuses them and adds more work for them.
- Program managers & directors that have been given ambiguous goals by their board of directors like "improve retention, increase engagement, create innovation, get people to collaborate." And who have no idea where to start or how to deliver on things like that.
- Program managers, directors, and vice presidents that are trying to understand how our technology and services fit into their existing technology and capability
- Employees who are bored and uninspired with their current tools and are hoping for some excitement in their life. Kind of like candy or a double espresso.
- Investors who think, our company like all the rest, are going to waste their money and make them look like a fool

Other information:
-The CSS and html needs to be responsive

-Our registration onboarding flow needs to collect this information:
User first name
user last name
user email
(verify their email)
user phone number
(verify their phone number)
User profile image (optional)
User profile summary (optional, like a bio, freeform text fiels)
If applicable: Register their organization
Organization name
Organization image (optional)
Account Mailing address
account Billing address (could be same as mailing address)
account Billing email address (could be same as user address)
account Product selection (pricing tier)
account Credit card information

The designs I am getting are a good start but they are only the front page. I just want you to know that I am expecting and need more than a landing page to complete the design. I will likely need a page that outlines the benefits and features of the product itself, how its different than our competitors, which will not be on the front page. I will need a registration flow. I will need a blog page design so we can post blog articles, I will need a team page, a page that goes into detail on our training, our services. I will likely need a page that shows all news and media we have been in. I need to show customer and user quotes, case studies, a way to contact us, partners, general resources like on collaboration, product tutorials, customers. I need the site to address a comprehensive set of needs. I need that design to be consistent and thorough. I know what LayoutBazaar is. I'm not using because I need more than a template that was customized. I need to be unique and match our brand thoughtfully, beautifully, and artistically. Someone asked me a question about how Brindle is similar to our tool in the way it is referred by end users and purchased by managers. Our website needs to primarily talk to the managers as I explained in the brief but it needs to appear cool and exciting to our end-users without focusing on the technology too much. Brindle is a tool that teams use to collaborate in small and large enterprises. The value prop for them is that communication is easier. But they don't put that on their website. Why? Because the users of the technology won't go to the website to find out information on it, they get their information from someone who is using it and demos it to them. When Nadia tells her manager Ted "Lets get brindle, Olga is using it at her company and its great" Nadia's manager doesn't know anything about brindle so she promptly googles it. The most important thing from Nadia's perspective is that Ted agrees to try it out. Ted's biggest concern is that productivity will be enhanced to degraded. Brindle knows this and so on the front page they know they are talking to Ted NOT Nadia because Nadia is already sold on it and doesn't need to get sold on the website. Nadia is end user. Ted is the purchaser. We have the same problem and so our end users are not the ones purchasing our product, their managers are purchasing our product. We get referred by our end users and vetted by their managers. Hope this helps! Thank you for looking at this project!  Added Wednesday, June 7, 2017

Another observation I am having about the designs being submitted. I believe we used the animations on our current website because animations / cartoons connect with the "inner child" in our users. Whatever that means :-). I think it's what makes our brand fun. I have a hard time imagining that we could make the design fun looking without animations but I'm sure it can be achieved. I also recognize that blending pictures of real people and animations is hard. So either we must masterfully blend them, use only animations, or make the real people have a LOT of fun! So far most of the designs while achieve the goal of appealing to the serious Vice Presidents and directors, they are not doing a good job at appealing to the overworked program managers and bored employees. There seems to stand another challenge with animations which is animations are hard to find and/or create that achieve the message / emotion we are trying to communicate. I don't have any good answers for this but I will say we can hire both animators and illustrators if we need to. All you have to do is communicate the effect in the website design with some simpler version maybe not the end illustration or animation itself. Added Wednesday, June 7, 2017

Industry/Entity Type

Saas

Coding

Coded - Design and coding required

Number of Pages Required

5+ page

Font styles to use
Sans Serif

Requirements
Must have
• Sex appeal and a sense of humor. Copy that makes people excited and clairvoyant about our potential.
Should not have
• Boring renditions of other non-inspiring websites

```html
<!DOCTYPE html>
<html lang="en">
<head>
<meta charset="utf-8">
<title>Velmora – Registration Form</title>
<link href="https://fonts.googleapis.com/css2?family=Open+Sans:wght@400;600;700;800&display=swap" rel="stylesheet">
<style>
:root{
  --blue:#3aaee3;
  --blue-dark:#2a9fd6;
  --green:#8cca7b;
  --green-dark:#74b862;
  --ink:#222;
  --label:#555;
  --line:#d9d9d9;
  --field-border:#c9c9c9;
  --page:#f4f4f4;
  --frame:#e3e3e3;
  --card-gray:#9a9a9a;
  --red:#e0231c;
  --white:#fff;
}
*{box-sizing:border-box;margin:0;padding:0}
html,body{width:1200px;height:2281px;overflow:hidden}
body{background:var(--frame);font-family:"Open Sans",Arial,sans-serif;color:var(--ink);position:relative}
.page{position:absolute;left:15px;top:15px;width:1171px;height:2250px;background:linear-gradient(160deg,#fafafa 0%,#efefef 40%,#f7f7f7 70%,#eeeeee 100%);overflow:hidden}
.abs{position:absolute}
/* header */
.topline{position:absolute;left:0;top:0;width:100%;height:3px;background:var(--blue)}
.utility-bar{position:absolute;left:723px;top:0;width:448px;height:26px;background:var(--blue);clip-path:polygon(4% 0,100% 0,100% 100%,0 100%);display:flex;align-items:center;gap:18px;padding-left:48px;font-size:12px;font-weight:600;color:var(--white)}
.utility-bar span{display:flex;align-items:center;gap:5px}
.utility-search{width:120px;height:15px;background:var(--white);border-radius:8px;margin-left:8px;position:relative}
.utility-search svg{position:absolute;right:5px;top:2px}
.brand{position:absolute;left:31px;top:50px;display:flex;align-items:center;gap:8px;font-size:30px;font-weight:700;color:var(--green)}
.brand-dot{width:34px;height:34px;border-radius:50%;background:var(--green)}
.main-nav{position:absolute;left:321px;top:64px;width:662px;display:flex;justify-content:space-between;font-size:10.5px;font-weight:700;color:#333;letter-spacing:-.2px;white-space:nowrap}
.demo-btn{position:absolute;left:1003px;top:57px;width:137px;height:30px;background:var(--blue);border-radius:4px;color:var(--white);font-size:13px;font-weight:700;display:flex;align-items:center;justify-content:center}
/* form */
.form-title{position:absolute;left:0;width:100%;top:146px;text-align:center;font-size:27px;font-weight:700;color:var(--ink)}
.form-title em{font-style:normal;color:var(--blue)}
.section-title{position:absolute;left:81px;font-size:14.5px;font-weight:700;color:var(--ink)}
.rule{position:absolute;left:79px;width:1026px;height:1px;background:var(--line)}
.vrule{position:absolute;width:1px;background:var(--line)}
.label{position:absolute;font-size:12.5px;font-weight:600;color:var(--label)}
.label b{color:var(--red);font-weight:700}
.input{position:absolute;height:32px;background:var(--white);border:1px solid var(--field-border);border-radius:3px}
.verified{position:absolute;right:8px;top:5px}
.textarea{position:absolute;background:var(--white);border:1px solid var(--field-border);border-radius:3px}
.select svg{position:absolute;right:0;top:0}
.avatar{position:absolute;width:95px;height:95px;background:#fff;border:1px solid #cfcfcf;padding:4px}
.avatar div{width:100%;height:100%;background:#9b9b9b;display:flex;align-items:flex-end;justify-content:center}
.hint{position:absolute;font-size:12.5px;color:#444}
.file-btn{position:absolute;width:104px;height:26px;background:var(--green);border:1px solid var(--green-dark);border-radius:2px;color:var(--white);font-size:11.5px;font-weight:700;display:flex;align-items:center;justify-content:center}
.radio{position:absolute;width:22px;height:22px;border:1.5px solid #555;border-radius:50%;background:var(--white)}
.radio.on::after{content:"";position:absolute;left:3px;top:3px;width:13px;height:13px;border-radius:50%;background:var(--blue)}
.option{position:absolute;font-size:13px;color:#444}
/* plans */
.plan{position:absolute;background:var(--white)}
.plan-head{color:var(--white);text-align:center}
.plan-name{font-size:14px;font-weight:600;padding-top:14px}
.plan-price{font-size:44px;font-weight:800;font-style:italic;line-height:1;margin-top:4px}
.plan-price small{font-size:24px;font-weight:600}
.plan-billing{font-size:16px;font-style:italic;font-weight:600;margin-top:6px}
.plan-features{list-style:none;padding:20px 0 0 42px;font-size:12.5px;font-weight:700;color:#222;line-height:22px}
.plan-features li{display:flex;align-items:center;gap:10px}
.plan-featured{left:94px;top:916px;width:271px;height:290px;border:7px solid var(--blue)}
.plan-featured .plan-head{background:var(--green);height:146px}
.plan-basic{left:379px;top:925px;width:252px;height:273px}
.plan-basic .plan-head{background:var(--card-gray);height:144px}
.pay-badges{position:absolute;left:998px;top:1570px;display:flex;gap:3px}
.pay-badges span{width:16px;height:11px;border-radius:2px;background:#9aa8c4}
.submit{position:absolute;left:96px;top:1827px;width:208px;height:29px;background:var(--blue);border:1px solid var(--blue-dark);border-radius:3px;color:var(--white);font-size:14px;font-weight:700;display:flex;align-items:center;justify-content:center}
/* footer */
.footer{position:absolute;left:0;top:1943px;width:1171px;height:278px;background:var(--blue);color:var(--white)}
.footer-brand{position:absolute;left:34px;top:104px;display:flex;align-items:center;gap:8px;font-size:25px;font-weight:700}
.footer-brand span.dot{width:34px;height:34px;border-radius:50%;background:var(--white)}
.footer-col{position:absolute;top:52px}
.footer-col h4{font-size:14.5px;font-weight:700;padding-bottom:10px;border-bottom:1px solid rgba(255,255,255,.7);margin-bottom:13px}
.footer-col ul{list-style:none;font-size:13px;font-weight:600;line-height:19.5px}
.contact-item{display:flex;gap:8px;font-size:13px;font-weight:600;line-height:18px;margin-bottom:14px}
.newsletter{display:flex}
.newsletter-input{width:161px;height:32px;background:var(--white);border:2px solid var(--green);color:#888;font-size:12px;display:flex;align-items:center;padding-left:8px}
.newsletter-btn{width:90px;height:32px;background:var(--green);font-size:14px;font-weight:700;display:flex;align-items:center;justify-content:center}
.mascot{position:absolute;left:1048px;top:1850px;width:100px;height:360px;border-radius:50px 50px 10px 10px;background:linear-gradient(180deg,#6b4a3a 0%,#3b9fd6 35%,#1f3f63 75%,#2b2b2b 100%);opacity:.85}
.legal-bar{position:absolute;left:0;top:2221px;width:1171px;height:29px;background:var(--green);color:var(--white);font-size:10.5px;font-weight:700;display:flex;align-items:center;padding-left:20px}
.social{position:absolute;right:16px;top:5px;display:flex;gap:6px}
.social span{width:20px;height:20px;border-radius:50%;border:1.5px solid var(--white)}
</style>
</head>
<body>
<div class="page">
  <header>
    <div class="topline"></div>
    <div class="utility-bar">
      <span>Contact</span><span>Register</span><span>Login</span>
      <div class="utility-search"><svg width="11" height="11" viewBox="0 0 11 11"><circle cx="4.5" cy="4.5" r="3.3" fill="none" stroke="#333" stroke-width="1.5"/><line x1="7" y1="7" x2="10" y2="10" stroke="#333" stroke-width="1.6"/></svg></div>
    </div>
    <div class="brand"><span class="brand-dot"></span>Velmora</div>
    <nav class="main-nav">
      <span>HOME</span><span>ABOUT US</span><span>SERVICES</span><span>PRODUCTS</span><span>WHO'S USING VELMORA</span><span>OUR EXPERIENCE</span><span>NEWS</span><span>RESOURCES ▾</span><span>SUPPORT</span>
    </nav>
    <div class="demo-btn">REQUEST A DEMO</div>
  </header>

  <main>
    <h1 class="form-title">Registration <em>Form</em></h1>

    <h2 class="section-title" style="top:221px">Personal Info</h2>
    <div class="rule" style="top:251px"></div>
    <div class="label" style="left:81px;top:263px">First Name:<b>*</b></div>
    <div class="input" style="left:79px;top:291px;width:226px"></div>
    <div class="vrule" style="left:323px;top:260px;height:80px"></div>
    <div class="label" style="left:343px;top:263px">Last Name:<b>*</b></div>
    <div class="input" style="left:341px;top:291px;width:225px"></div>
    <div class="vrule" style="left:584px;top:260px;height:80px"></div>
    <div class="label" style="left:605px;top:263px">Email Address:<b>*</b></div>
    <div class="input" style="left:603px;top:291px;width:225px"><svg class="verified" width="21" height="21" viewBox="0 0 21 21"><circle cx="10.5" cy="10.5" r="10" fill="var(--red)"/><path d="M5.5 10.5l3.5 3.5 6.5-7" fill="none" stroke="#fff" stroke-width="2.6"/></svg></div>
    <div class="vrule" style="left:846px;top:260px;height:80px"></div>
    <div class="label" style="left:866px;top:263px">Phone Number:<b>*</b></div>
    <div class="input" style="left:864px;top:291px;width:226px"><svg class="verified" width="21" height="21" viewBox="0 0 21 21"><circle cx="10.5" cy="10.5" r="10" fill="var(--red)"/><path d="M5.5 10.5l3.5 3.5 6.5-7" fill="none" stroke="#fff" stroke-width="2.6"/></svg></div>
    <div class="rule" style="top:338px"></div>

    <div class="label" style="left:81px;top:356px">Profile Image</div>
    <div class="avatar" style="left:81px;top:377px"><div><svg width="60" height="70" viewBox="0 0 60 70"><circle cx="30" cy="22" r="14" fill="#6f6f6f"/><path d="M4 70c0-20 10-30 26-30s26 10 26 30z" fill="#6f6f6f"/></svg></div></div>
    <div class="hint" style="left:193px;top:388px">The image must not exceed 1MB</div>
    <div class="file-btn" style="left:192px;top:409px">Choose File</div>
    <div class="vrule" style="left:428px;top:350px;height:152px"></div>
    <div class="label" style="left:457px;top:359px">Profile Summary</div>
    <div class="textarea" style="left:453px;top:380px;width:637px;height:107px"></div>
    <div class="rule" style="top:504px"></div>

    <div class="label" style="left:81px;top:523px">Why are you registering:<b>*</b></div>
    <svg class="abs" style="left:80px;top:551px" width="34" height="26" viewBox="0 0 34 26"><g fill="var(--blue)"><circle cx="17" cy="3.5" r="3"/><rect x="13" y="7" width="8" height="6" rx="2"/><rect x="4" y="15" width="26" height="1.5"/><circle cx="5" cy="19" r="2.4"/><circle cx="17" cy="19" r="2.4"/><circle cx="29" cy="19" r="2.4"/><rect x="2" y="21.5" width="6" height="4" rx="1.5"/><rect x="14" y="21.5" width="6" height="4" rx="1.5"/><rect x="26" y="21.5" width="6" height="4" rx="1.5"/></g></svg>
    <div class="radio" style="left:123px;top:551px"></div>
    <div class="option" style="left:153px;top:553px">Launching an organization / community</div>
    <svg class="abs" style="left:447px;top:554px" width="36" height="18" viewBox="0 0 36 18"><g fill="none" stroke="var(--blue)" stroke-width="1.6"><circle cx="9" cy="5" r="3"/><circle cx="18" cy="4" r="3"/><circle cx="27" cy="5" r="3"/><path d="M4 17c0-5 2-8 5-8s5 3 5 8M13 17c0-5 2-8 5-8s5 3 5 8M22 17c0-5 2-8 5-8s5 3 5 8"/></g></svg>
    <div class="radio on" style="left:491px;top:551px"></div>
    <div class="option" style="left:521px;top:553px">Joining an organization / community</div>
    <svg class="abs" style="left:794px;top:554px" width="34" height="18" viewBox="0 0 34 18"><path d="M2 9C8 1 26 1 32 9 26 17 8 17 2 9z" fill="var(--blue)"/><circle cx="17" cy="9" r="5" fill="#fff"/><circle cx="17" cy="9" r="2.6" fill="var(--blue)"/></svg>
    <div class="radio" style="left:838px;top:551px"></div>
    <div class="option" style="left:868px;top:553px">Just checking it out</div>
    <div class="rule" style="top:593px"></div>

    <h2 class="section-title" style="top:642px">Organization Info</h2>
    <div class="rule" style="top:663px"></div>
    <div class="label" style="left:81px;top:682px">Organization Name:<b>*</b></div>
    <div class="input" style="left:79px;top:703px;width:577px"></div>
    <div class="vrule" style="left:685px;top:672px;height:140px"></div>
    <div class="label" style="left:714px;top:682px">Organization Image</div>
    <div class="avatar" style="left:714px;top:704px"><div><svg width="60" height="70" viewBox="0 0 60 70"><circle cx="30" cy="22" r="14" fill="#6f6f6f"/><path d="M4 70c0-20 10-30 26-30s26 10 26 30z" fill="#6f6f6f"/></svg></div></div>
    <div class="hint" style="left:826px;top:712px">The image must not exceed 1MB</div>
    <div class="file-btn" style="left:823px;top:735px">Choose File</div>
    <div class="rule" style="top:814px"></div>

    <h2 class="section-title" style="top:863px">Product Selection<b style="color:var(--red)">*</b></h2>
    <div class="rule" style="top:882px"></div>
    <div class="plan plan-featured">
      <div class="plan-head"><div class="plan-name">Consistent - Usage - Starter</div><div class="plan-price">$50<small>/mo</small></div><div class="plan-billing">billed monthly</div></div>
      <ul class="plan-features">
        <li><svg width="18" height="14" viewBox="0 0 18 14"><path d="M1 7l5 5L17 1" fill="none" stroke="var(--green-dark)" stroke-width="3"/></svg>Free For 30 days</li>
        <li><svg width="18" height="14" viewBox="0 0 18 14"><path d="M1 7l5 5L17 1" fill="none" stroke="var(--green-dark)" stroke-width="3"/></svg>Unlimited Users</li>
        <li><svg width="18" height="14" viewBox="0 0 18 14"><path d="M1 7l5 5L17 1" fill="none" stroke="var(--green-dark)" stroke-width="3"/></svg>1500 Active Connections</li>
        <li><svg width="18" height="14" viewBox="0 0 18 14"><path d="M1 7l5 5L17 1" fill="none" stroke="var(--green-dark)" stroke-width="3"/></svg>75 Meetings</li>
      </ul>
    </div>
    <svg class="abs" style="left:308px;top:1001px" width="24" height="30" viewBox="0 0 24 30"><path d="M7 2c1.5 0 2.5 1 2.5 2.5V13l1-1c1.5-.5 2.5 0 3 1 1.2-.6 2.4-.2 3 .8 1.3-.5 2.8.2 3 1.8V22c0 4-3 7-7 7h-2c-3 0-4.5-1.5-6-4L1 18c-.6-1.2.6-2.5 2-1.8L4.5 18V4.5C4.5 3 5.5 2 7 2z" fill="#fff" stroke="#000" stroke-width="1.4"/></svg>
    <div class="plan plan-basic">
      <div class="plan-head"><div class="plan-name">Consistent - Usage - Pro</div><div class="plan-price">$100<small>/mo</small></div><div class="plan-billing">billed monthly</div></div>
      <ul class="plan-features">
        <li><svg width="18" height="14" viewBox="0 0 18 14"><path d="M1 7l5 5L17 1" fill="none" stroke="var(--green-dark)" stroke-width="3"/></svg>Free For 30 days</li>
        <li><svg width="18" height="14" viewBox="0 0 18 14"><path d="M1 7l5 5L17 1" fill="none" stroke="var(--green-dark)" stroke-width="3"/></svg>Unlimited Users</li>
        <li><svg width="18" height="14" viewBox="0 0 18 14"><path d="M1 7l5 5L17 1" fill="none" stroke="var(--green-dark)" stroke-width="3"/></svg>5k Active Connections</li>
        <li><svg width="18" height="14" viewBox="0 0 18 14"><path d="M1 7l5 5L17 1" fill="none" stroke="var(--green-dark)" stroke-width="3"/></svg>75 Meetings</li>
      </ul>
    </div>
    <div class="rule" style="top:1206px"></div>

    <h2 class="section-title" style="top:1253px">Account Mailing &amp; Billing Address</h2>
    <div class="rule" style="top:1275px"></div>
    <div class="vrule" style="left:584px;top:1275px;height:239px"></div>
    <div class="label" style="left:81px;top:1294px">Mailing Address:<b>*</b></div>
    <div class="input" style="left:79px;top:1314px;width:488px"></div>
    <div class="label" style="left:605px;top:1294px">Billing Address:<b>*</b></div>
    <div class="radio" style="left:908px;top:1292px;width:21px;height:21px"></div>
    <div class="option" style="left:937px;top:1294px;font-size:12.5px">Same as mailing address</div>
    <div class="input" style="left:603px;top:1314px;width:488px"></div>

    <div class="label" style="left:81px;top:1371px">City:<b>*</b></div>
    <div class="input" style="left:79px;top:1392px;width:236px"></div>
    <div class="label" style="left:334px;top:1371px">State/Province/Region:<b>*</b></div>
    <div class="input" style="left:332px;top:1392px;width:235px"></div>
    <div class="label" style="left:605px;top:1371px">City:<b>*</b></div>
    <div class="input" style="left:603px;top:1392px;width:236px"></div>
    <div class="label" style="left:858px;top:1371px">State/Province/Region:<b>*</b></div>
    <div class="input" style="left:856px;top:1392px;width:235px"></div>

    <div class="label" style="left:81px;top:1448px">Zip/Postal Code:<b>*</b></div>
    <div class="input" style="left:79px;top:1468px;width:236px"></div>
    <div class="label" style="left:334px;top:1448px">Country:<b>*</b></div>
    <div class="input select" style="left:332px;top:1468px;width:235px"><svg width="30" height="30" viewBox="0 0 30 30"><line x1="0" y1="4" x2="0" y2="26" stroke="#ccc"/><path d="M9 12h12l-6 7z" fill="#555"/></svg></div>
    <div class="label" style="left:605px;top:1448px">Zip/Postal Code:<b>*</b></div>
    <div class="input" style="left:603px;top:1468px;width:236px"></div>
    <div class="label" style="left:858px;top:1448px">Country:<b>*</b></div>
    <div class="input select" style="left:856px;top:1468px;width:235px"><svg width="30" height="30" viewBox="0 0 30 30"><line x1="0" y1="4" x2="0" y2="26" stroke="#ccc"/><path d="M9 12h12l-6 7z" fill="#555"/></svg></div>
    <div class="rule" style="top:1514px"></div>

    <h2 class="section-title" style="top:1561px">Payment Information</h2>
    <div class="pay-badges"><span></span><span></span><span></span><span></span><span></span></div>
    <div class="rule" style="top:1582px"></div>
    <div class="vrule" style="left:584px;top:1582px;height:84px"></div>
    <div class="label" style="left:81px;top:1600px">First Name:<b>*</b></div>
    <div class="input" style="left:79px;top:1622px;width:488px"></div>
    <div class="label" style="left:605px;top:1600px">Last Name:<b>*</b></div>
    <div class="input" style="left:603px;top:1622px;width:488px"></div>
    <div class="rule" style="top:1666px"></div>
    <div class="vrule" style="left:584px;top:1666px;height:86px"></div>
    <div class="vrule" style="left:785px;top:1666px;height:86px"></div>
    <div class="label" style="left:81px;top:1687px">Credit Card Number:<b>*</b></div>
    <div class="input" style="left:79px;top:1707px;width:488px"></div>
    <div class="label" style="left:605px;top:1687px">CVV Code:<b>*</b></div>
    <div class="input" style="left:603px;top:1707px;width:162px"></div>
    <div class="label" style="left:803px;top:1687px">Card Expiration Date:<b>*</b></div>
    <div class="input select" style="left:802px;top:1707px;width:135px;font-size:13px;color:#444;padding:7px 0 0 8px">January<svg width="30" height="30" viewBox="0 0 30 30"><line x1="0" y1="4" x2="0" y2="26" stroke="#ccc"/><path d="M9 12h12l-6 7z" fill="#555"/></svg></div>
    <div class="input select" style="left:954px;top:1707px;width:137px;font-size:13px;color:#444;padding:7px 0 0 12px">2018<svg width="30" height="30" viewBox="0 0 30 30"><line x1="0" y1="4" x2="0" y2="26" stroke="#ccc"/><path d="M9 12h12l-6 7z" fill="#555"/></svg></div>
    <div class="rule" style="top:1752px"></div>

    <div class="radio" style="left:81px;top:1771px"></div>
    <div class="option" style="left:109px;top:1773px">I understand the terms of use and policy</div>
    <div class="submit">SUBMIT</div>
  </main>

  <footer class="footer">
    <div class="footer-brand"><span class="dot"></span>Velmora</div>
    <div class="footer-col" style="left:227px">
      <h4>QUICK LINKS</h4>
      <ul><li>Home</li><li>About Us</li><li>Services</li><li>Products</li><li>Support</li><li>Blog</li><li>Request A Demo</li></ul>
    </div>
    <div class="footer-col" style="left:385px">
      <h4>OUR SOLUTIONS</h4>
      <ul><li>Custom Built Solutions</li><li>Training</li><li>Consulting</li><li>Tools</li></ul>
    </div>
    <div class="footer-col" style="left:578px;width:157px">
      <h4>CONTACT</h4>
      <div class="contact-item"><svg width="18" height="18" viewBox="0 0 18 18"><circle cx="9" cy="9" r="8" fill="none" stroke="#fff" stroke-width="1.4"/><path d="M9 4a3 3 0 0 1 3 3c0 2.3-3 6-3 6S6 9.3 6 7a3 3 0 0 1 3-3z" fill="#fff"/></svg><div>Velmora<br>48 Harlow Lane<br>Pasadena, CA 91105</div></div>
      <div class="contact-item"><svg width="18" height="18" viewBox="0 0 18 18"><circle cx="9" cy="9" r="8" fill="none" stroke="#fff" stroke-width="1.4"/><path d="M6 5l2 2-1 1.3c.6 1.2 1.5 2.1 2.7 2.7L11 10l2 2-1.3 1.3C9 13 5 9 4.7 6.3z" fill="#fff"/></svg><div>(800) 555-0142</div></div>
      <div class="contact-item"><svg width="18" height="18" viewBox="0 0 18 18"><circle cx="9" cy="9" r="8" fill="none" stroke="#fff" stroke-width="1.4"/><rect x="5" y="6" width="8" height="6" fill="none" stroke="#fff" stroke-width="1.2"/><path d="M5 6l4 3 4-3" fill="none" stroke="#fff" stroke-width="1.2"/></svg><div>info@velmorahub.com</div></div>
    </div>
    <div class="footer-col" style="left:791px;width:251px">
      <h4>NEWSLETTER</h4>
      <div class="newsletter"><div class="newsletter-input">Enter Email Address</div><div class="newsletter-btn">SIGN UP</div></div>
    </div>
  </footer>
  <div class="mascot" role="img" aria-label="Illustrated character of a friendly businesswoman in a blue blazer holding a folder, gesturing toward the sign-up area"></div>
  <div class="legal-bar">COPYRIGHT © 2017 VELMORA. ALL RIGHTS RESERVED.
    <div class="social"><span></span><span></span><span></span></div>
  </div>
</div>
</body>
</html>
```